Updated Business Cards

We need to update our business cards to reflect new services and employees. We are a luxury vacation rental company in Sandpoint, Idaho. Would also like to make the front facing font easier to read (larger fonts) I love the original logo created for our company and want to use this for the back of the business card created like before - with the dark blue color. See previous files.

Front of the card needs to include:
Employee Name
Title
Phone: 208-555-0147 (ext X)
Address: 418 W. Larkmoor St, Ste 5
Sandpoint, ID 83871
Book Direct: www.RestWillowbay.example

```html
<!DOCTYPE html>
<html lang="en">
<head>
<meta charset="utf-8">
<title>Halvorsen Management – Business Cards</title>
<link rel="stylesheet" href="https://fonts.googleapis.com/css2?family=EB+Garamond:wght@400;500&display=swap">
<style>
  :root {
    --navy: #1f2a6b;
    --ink: #55585e;
    --rule: #6b6e74;
    --card: #ffffff;
    --bg-light: #c4c5c8;
    --bg-dark: #8e9093;
  }
  * { box-sizing: border-box; margin: 0; padding: 0; }
  html, body { width: 1200px; height: 781px; overflow: hidden; }
  body {
    background: radial-gradient(ellipse at 55% 45%, var(--bg-light), var(--bg-dark));
    font-family: "EB Garamond", Georgia, serif;
    position: relative;
  }
  .card {
    position: absolute;
    width: 525px;
    height: 300px;
    background: var(--card);
    box-shadow: 0 1px 0 #e6e6e8, 0 3px 0 #d8d8da, 0 5px 0 #e6e6e8, 0 14px 28px rgba(0,0,0,.28);
  }
  .card--front { left: 45px; top: 300px; }
  .card--back  { left: 630px; top: 170px; }

  .wordmark {
    color: var(--navy);
    font-weight: 500;
    text-transform: uppercase;
    text-align: center;
    line-height: 1.05;
  }
  .wordmark__name { display: block; letter-spacing: .04em; }
  .wordmark__sub  { display: block; letter-spacing: .32em; }

  .card--front .wordmark {
    position: absolute; left: 70px; top: 40px; width: 190px;
  }
  .card--front .wordmark__name { font-size: 24px; }
  .card--front .wordmark__sub  { font-size: 12px; margin-top: 4px; }

  .card--back .wordmark {
    position: absolute; left: 0; right: 0; top: 112px;
  }
  .card--back .wordmark__name { font-size: 44px; }
  .card--back .wordmark__sub  { font-size: 18px; margin-top: 8px; }

  .address {
    position: absolute; left: 34px; top: 140px;
    color: var(--ink); font-size: 13px; line-height: 1.45;
  }
  .person {
    position: absolute; left: 300px; top: 128px;
  }
  .person__name {
    color: var(--navy); font-size: 19px; font-weight: 500;
    font-variant: small-caps; letter-spacing: .03em;
  }
  .person__title { color: var(--ink); font-size: 12px; margin-top: 1px; }

  .contacts {
    position: absolute; left: 245px; top: 212px;
    list-style: none; color: var(--ink); font-size: 15px; line-height: 1.55;
  }
  .contacts li { display: flex; align-items: center; gap: 8px; }
  .contacts svg { width: 13px; height: 13px; flex: none; }
</style>
</head>
<body>
  <section class="card card--front" aria-label="Business card front">
    <div class="wordmark">
      <span class="wordmark__name">Halvorsen</span>
      <span class="wordmark__sub">Management</span>
    </div>
    <p class="address">418 W. Larkmoor St, Ste 5<br>Sandpoint, ID 83871</p>
    <div class="person">
      <p class="person__name">Marlo Halvorsen</p>
      <p class="person__title">President</p>
    </div>
    <ul class="contacts">
      <li>
        <svg viewBox="0 0 16 16" aria-hidden="true"><path fill="#3a3d44" d="M4 1.5l2.2 3-1.3 1.6a8 8 0 0 0 5 5l1.6-1.3 3 2.2-1.3 2.3C8 14.5 1.5 8 1.7 2.8z"/></svg>
        <span>208-555-0147 (ext X)</span>
      </li>
      <li>
        <svg viewBox="0 0 16 16" aria-hidden="true"><rect x="1" y="3" width="14" height="10" fill="#3a3d44"/><path d="M1 3l7 6 7-6" fill="none" stroke="#fff" stroke-width="1.2"/></svg>
        <span>Marlo@RestWillowbay.example</span>
      </li>
      <li>
        <svg viewBox="0 0 16 16" aria-hidden="true"><circle cx="8" cy="8" r="7" fill="#3a3d44"/><g fill="none" stroke="#fff" stroke-width=".9"><ellipse cx="8" cy="8" rx="3" ry="6.5"/><path d="M1.5 8h13M2.5 5h11M2.5 11h11"/></g></svg>
        <span>www.RestWillowbay.example</span>
      </li>
    </ul>
  </section>

  <section class="card card--back" aria-label="Business card back">
    <div class="wordmark">
      <span class="wordmark__name">Halvorsen</span>
      <span class="wordmark__sub">Management</span>
    </div>
  </section>
</body>
</html>
```